Poloshirt Packaging

We need a very attractive packaging design for our poloshirts. We are wholesaler of the schoolwear market. See what we currently have. I dont want any specific sizing put on the packaging. One design for all poloshirts (2 sides).
our logo is attached aswell

Target Market(s)

Parents

Requirements
Must have
• Our logo
Should not have
• size or age

```html
<!DOCTYPE html>
<html lang="en">
<head>
<meta charset="utf-8">
<title>Brightstride Poloshirt Packaging</title>
<link rel="stylesheet" href="https://fonts.googleapis.com/css2?family=Oswald:wght@300;500;700&display=swap">
<style>
  :root {
    --paper: #ffffff;
    --frame: #2a2a2a;
    --brand-navy: #15375f;
    --brand-red: #e3202e;
    --band-text: #ffffff;
  }
  html, body {
    margin: 0;
    padding: 0;
    overflow: hidden;
    background: var(--paper);
  }
  .pack-face {
    position: relative;
    width: 849px;
    height: 1200px;
    box-sizing: border-box;
    border: 1px solid var(--frame);
    background: var(--paper);
    overflow: hidden;
    font-family: "Oswald", "Arial Narrow", sans-serif;
  }
  .brand-name {
    position: absolute;
    top: 350px;
    left: 0;
    width: 100%;
    margin: 0;
    text-align: center;
    font-weight: 500;
    font-size: 92px;
    line-height: 1;
    letter-spacing: 1px;
    color: var(--brand-navy);
  }
  .product-title {
    position: absolute;
    top: 752px;
    left: 0;
    width: 100%;
    margin: 0;
    text-align: center;
    font-weight: 700;
    font-size: 78px;
    line-height: 1;
    letter-spacing: 0.5px;
    color: var(--brand-red);
  }
  .thanks-band {
    position: absolute;
    top: 1035px;
    left: 99px;
    width: 651px;
    height: 89px;
    background: var(--brand-red);
    color: var(--band-text);
    display: flex;
    flex-direction: column;
    justify-content: center;
    align-items: center;
    text-align: center;
  }
  .thanks-band p {
    margin: 0;
    font-weight: 300;
    font-size: 21px;
    line-height: 40px;
    letter-spacing: 0.2px;
  }
</style>
</head>
<body>
  <main class="pack-face">
    <h1 class="brand-name">Brightstride</h1>
    <h2 class="product-title">POLOSHIRT</h2>
    <div class="thanks-band">
      <p>Thanks You for Buying Our Product and Ask your Local Supplier</p>
      <p>abt the Rest Of Brightstride Range</p>
    </div>
  </main>
</body>
</html>
```